Divi Theme Wordpress Web Design

Hi,

We have had a Divi theme website running on Wordpress for a few years but need a fresh refresh.

Designs must be possible with standard Divi theme and minimal/no CSS customisation or similar. if this is required please note this in submission. Also, please note mobile and device usage which must be universal.

We have our logo files attached, plus some research and sample sites we have done, plus all of our current collateral. We will need a few examples such as landing (main) page, single blog post and software specific page. See current examples below:

Landing (Main) - http://www.pelrandata.example/inventory-wholesale-manufacturing/

Single Blog Post - http://www.pelrandata.example/why-remote-work-made-break-most-relaxing-ever/

Software Page - http://www.pelrandata.example/software-implementation/tolvek-stock-implementation-and-training/

Target Market(s)

small businesses, small business owners, people who need simple but technical computer help,

Industry/Entity Type

Professional Service

Number of Pages Required

3 page

Requirements
Must have
• see attachment guide
Nice to have
• see attachment guide

```html
<!DOCTYPE html>
<html lang="en">
<head>
<meta charset="utf-8">
<title>Pelran Data</title>
<link href="https://fonts.googleapis.com/css2?family=Roboto:wght@300;400;500&family=Open+Sans:wght@400;600&display=swap" rel="stylesheet">
<style>
:root{
  --teal:#2a9fb0;
  --navy:#1d4f73;
  --orange:#f07c34;
  --red:#a51f2e;
  --ink:#333;
  --muted:#777;
  --light:#f4f5f7;
  --line:#e2e4e8;
  --footer:#3a3a3a;
}
*{box-sizing:border-box;margin:0;padding:0}
html,body{width:1200px;height:3696px;overflow:hidden}
body{font-family:"Open Sans",Arial,sans-serif;color:var(--ink);background:#fff;font-size:14px}
h1,h2,h3,h4{font-family:"Roboto",Arial,sans-serif;font-weight:400}
.wrap{width:1030px;margin:0 auto;position:relative}
section{position:relative;overflow:hidden}
.sec-title{text-align:center;font-size:27px;color:#444;padding-top:52px}
.sec-title span{color:var(--teal)}
.sec-lead{text-align:center;font-size:12.5px;color:var(--muted);line-height:26px;width:520px;margin:18px auto 0}

/* header */
.site-header{height:98px;display:flex;align-items:center;justify-content:space-between;padding:0 86px;background:#fff}
.brand{display:flex;align-items:center;gap:12px;font-family:"Roboto",sans-serif;font-weight:500;font-size:27px;color:var(--navy)}
.brand-dot{width:34px;height:34px;border-radius:50%;background:var(--teal)}
.main-nav{display:flex;align-items:center;gap:48px;font-size:11.5px;color:#555;text-transform:uppercase}
.main-nav .active{color:var(--orange)}
.search-btn{width:40px;height:40px;border:1.5px solid var(--orange);border-radius:50%;display:flex;align-items:center;justify-content:center}

/* hero */
.hero{height:510px;background:linear-gradient(120deg,#3b3f46 0%,#1e2024 45%,#4a4339 100%);color:#fff;text-align:center}
.hero h1{font-size:64px;font-weight:400;padding-top:160px}
.hero p{font-size:15px;line-height:26px;width:620px;margin:22px auto 0}
.btn-teal{display:inline-block;margin-top:24px;background:var(--teal);color:#fff;font-size:14px;padding:12px 30px;border-radius:3px;text-transform:uppercase}
.dots{position:absolute;bottom:16px;left:50%;transform:translateX(-50%);display:flex;gap:6px}
.dots i{width:13px;height:13px;border:2px solid #fff;border-radius:50%}
.dots i.on{background:var(--teal)}

/* trust */
.trust{height:407px}
.questions{display:flex;justify-content:space-around;margin-top:36px}
.question{width:220px;text-align:center;font-size:14px;line-height:22px}
.q-ring{width:118px;height:118px;border-radius:50%;margin:0 auto 12px;display:flex;align-items:center;justify-content:center;border:5px solid #fff;box-shadow:0 0 0 2px currentColor}
.q-teal{color:var(--teal)} .q-navy{color:var(--navy)} .q-orange{color:var(--orange)} .q-red{color:var(--red)}
.q-teal .q-ring{background:var(--teal)} .q-navy .q-ring{background:var(--navy)}
.q-orange .q-ring{background:var(--orange)} .q-red .q-ring{background:var(--red)}

/* team */
.team{height:466px;background:var(--light)}
.members{display:flex;justify-content:space-around;margin-top:38px;padding:0 60px}
.member{text-align:center;width:240px}
.member .photo{width:190px;height:190px;border-radius:50%;border:6px solid #fff;box-shadow:0 0 0 1px #ddd;margin:0 auto;background:radial-gradient(circle at 50% 40%,#b88f74,#5c5247 70%)}
.member h4{font-size:15px;margin-top:22px;color:#444}
.member p{font-size:12px;color:var(--muted);margin-top:4px}

/* process */
.process{height:424px;background:linear-gradient(135deg,#2aa3b4,#1f93a5);color:#fff}
.process .sec-title{color:#fff;padding-top:30px}
.process .sec-lead{color:#e6f6f8;margin-top:10px}
.steps{display:flex;justify-content:space-between;margin-top:28px;padding:0 10px}
.step{width:190px;text-align:center}
.step .ring{width:112px;height:112px;border:2px solid #fff;border-radius:50%;margin:0 auto;display:flex;align-items:center;justify-content:center}
.step h4{font-size:17px;margin-top:14px}
.step p{font-size:11.5px;line-height:21px;margin-top:6px}

/* blog */
.blog{height:584px}
.posts{display:flex;justify-content:space-between;margin-top:36px}
.post{width:324px}
.post .thumb{height:206px}
.post h4{font-size:14px;margin-top:22px;color:#333}
.meta{margin-top:14px;padding-bottom:10px;border-bottom:1px solid var(--line);font-size:9.5px;color:#999;display:flex;gap:24px}
.post p{font-size:11.5px;line-height:21px;color:#555;margin-top:14px}

/* clients */
.clients{height:426px;background:var(--light)}
.logos{display:grid;grid-template-columns:repeat(5,1fr);margin-top:34px;row-gap:38px}
.logo{height:48px;display:flex;align-items:center;justify-content:center;border-right:1px solid var(--line);font-family:"Roboto",sans-serif;font-weight:500;font-size:17px;color:#3d3d3d}
.logo:nth-child(5n){border-right:none}

/* testimonial */
.testimonial{height:276px;background:linear-gradient(135deg,#f07c34,#ea6f26);color:#fff}
.testimonial .wrap{display:flex;align-items:center;height:100%;padding-left:78px}
.t-photo{width:134px;height:134px;border-radius:50%;border:5px solid #fff;background:radial-gradient(circle at 50% 40%,#e8d2c2,#9c8575 75%);flex:none}
.t-body{margin-left:40px;position:relative;width:760px}
.t-body blockquote{font-size:12px;line-height:24px;padding-left:14px}
.quote{font-family:"Roboto",sans-serif;font-size:38px;position:absolute;line-height:1}
.q-open{left:-16px;top:-10px} .q-close{right:60px;bottom:10px}
.t-name{font-size:11.5px;font-weight:600;margin-top:8px;padding-left:14px}
.t-role{font-size:10.5px;padding-left:14px;margin-top:2px}
.stars{padding-left:14px;margin-top:6px;display:flex;gap:4px}

/* contact */
.contact{height:439px}
.contact .sec-title{padding-top:28px}
.contact .sec-lead{width:800px;margin-top:8px}
.contact-grid{display:flex;justify-content:space-between;margin-top:52px}
.form{width:500px;display:grid;grid-template-columns:1fr 1fr;gap:14px 16px}
.field{height:38px;border:1px solid var(--line);background:#f7f8fa;font-size:10.5px;color:#888;padding:12px 14px}
.field.msg{grid-column:1/3;height:110px}
.submit{background:var(--red);color:#fff;font-size:12px;font-weight:600;width:106px;height:40px;display:flex;align-items:center;justify-content:center;border-radius:3px;margin-top:6px}
.info{width:500px;font-size:11.5px;color:#666;line-height:21px}
.info-cols{display:grid;grid-template-columns:1fr 1fr;margin-top:14px;gap:14px 20px}
.info h5{font-family:"Roboto",sans-serif;font-weight:500;font-size:12px;color:var(--teal);text-transform:uppercase;margin-bottom:6px}
.social{display:flex;gap:8px}
.social i{width:30px;height:30px;border:1px solid #bbb;border-radius:50%}

.site-footer{height:66px;background:var(--footer);color:#ddd;font-size:11.5px;display:flex;align-items:center;justify-content:center}
</style>
</head>
<body>

<header class="site-header">
  <div class="brand"><span class="brand-dot"></span>Pelran Data</div>
  <nav class="main-nav">
    <span class="active">Home</span><span>About Us</span><span>Blog</span><span>Software Solutions</span><span>Contact Us</span>
    <span class="search-btn"><svg width="16" height="16" viewBox="0 0 16 16"><circle cx="7" cy="7" r="5" fill="none" stroke="#f07c34" stroke-width="2"/><line x1="11" y1="11" x2="15" y2="15" stroke="#f07c34" stroke-width="2"/></svg></span>
  </nav>
</header>

<section class="hero" role="img" aria-label="Dark photograph of hands using a laptop and smartphone">
  <h1>Pelran Data</h1>
  <p>Our Ledgerly Add-On Solutions help ambitious businesses who want to take control of their removing the guess work and enabling them to make better decisions.</p>
  <span class="btn-teal">Read More</span>
  <div class="dots"><i></i><i class="on"></i><i></i></div>
</section>

<section class="trust">
  <h2 class="sec-title">Do you REALLY Trust <span>Your Inventory System?</span></h2>
  <p class="sec-lead">For businesses on the Ledgerly platform who manage inventory, our Scoping Consultation is the first step to finally control your inventory with confidence.</p>
  <div class="wrap questions">
    <div class="question q-teal"><div class="q-ring"><svg width="50" height="44" viewBox="0 0 50 44" fill="none" stroke="#fff" stroke-width="3"><rect x="3" y="3" width="44" height="38"/><line x1="14" y1="34" x2="14" y2="22"/><line x1="22" y1="34" x2="22" y2="14"/><line x1="30" y1="34" x2="30" y2="18"/><line x1="38" y1="34" x2="38" y2="10"/></svg></div>Are those stock levels accurate?</div>
    <div class="question q-navy"><div class="q-ring"><svg width="34" height="50" viewBox="0 0 34 50" fill="none" stroke="#fff" stroke-width="3"><rect x="3" y="3" width="28" height="44"/><rect x="10" y="10" width="5" height="5"/><rect x="19" y="10" width="5" height="5"/><rect x="10" y="20" width="5" height="5"/><rect x="19" y="20" width="5" height="5"/><rect x="13" y="35" width="8" height="12"/></svg></div>Does the Hobart warehouse have stock?</div>
    <div class="question q-orange"><div class="q-ring"><svg width="52" height="46" viewBox="0 0 52 46" fill="none" stroke="#fff" stroke-width="3"><rect x="3" y="3" width="46" height="30"/><line x1="26" y1="33" x2="26" y2="42"/><line x1="14" y1="43" x2="38" y2="43"/></svg></div>How many do we need to order?</div>
    <div class="question q-red"><div class="q-ring"><svg width="46" height="46" viewBox="0 0 46 46" fill="none" stroke="#fff" stroke-width="3"><rect x="3" y="9" width="32" height="32" rx="4"/><path d="M18 28 L20 20 L38 3 L43 8 L25 25 Z"/></svg></div>Why have we sold so much of that product?</div>
  </div>
</section>

<section class="team">
  <h2 class="sec-title">About <span>Our Team</span></h2>
  <p class="sec-lead">For businesses on the Ledgerly platform who manage inventory, our Scoping Consultation is the first step to finally control your inventory with confidence.</p>
  <div class="wrap members">
    <div class="member"><div class="photo" role="img" aria-label="Portrait photograph of Tom Werrick"></div><h4>Tom Werrick</h4><p>Operations Manager</p></div>
    <div class="member"><div class="photo" role="img" aria-label="Portrait photograph of Joel Harnett"></div><h4>Joel Harnett</h4><p>Client Service Manager</p></div>
    <div class="member"><div class="photo" role="img" aria-label="Portrait photograph of Owen Calder"></div><h4>Owen Calder</h4><p>Client Project Manager</p></div>
  </div>
</section>

<section class="process">
  <h2 class="sec-title">Our Process</h2>
  <p class="sec-lead">For businesses on the Ledgerly platform who manage inventory, our Scoping Consultation is the first step to finally control your inventory with confidence.</p>
  <div class="wrap steps">
    <div class="step"><div class="ring"><svg width="44" height="34" viewBox="0 0 44 34" fill="#fff"><circle cx="22" cy="9" r="7"/><circle cx="8" cy="12" r="5"/><circle cx="36" cy="12" r="5"/><path d="M10 34 a12 12 0 0 1 24 0Z"/><path d="M0 32 a8 8 0 0 1 12 -8 l-2 8Z"/><path d="M44 32 a8 8 0 0 0 -12 -8 l2 8Z"/></svg></div><h4>Scoping</h4><p>For businesses on the Ledgerly platform who manage inventory with confidence.</p></div>
    <div class="step"><div class="ring"><svg width="32" height="40" viewBox="0 0 32 40" fill="none" stroke="#fff" stroke-width="2.5"><path d="M3 3 H21 L29 11 V37 H3Z"/><line x1="9" y1="18" x2="23" y2="18"/><line x1="9" y1="24" x2="23" y2="24"/><line x1="9" y1="30" x2="23" y2="30"/></svg></div><h4>Implementation</h4><p>For businesses on the Ledgerly platform who manage inventory with confidence.</p></div>
    <div class="step"><div class="ring"><svg width="46" height="32" viewBox="0 0 46 32" fill="none" stroke="#fff" stroke-width="2.5"><rect x="8" y="3" width="30" height="20"/><path d="M2 28 H44 L40 23 H6Z"/></svg></div><h4>Training</h4><p>For businesses on the Ledgerly platform who manage inventory with confidence.</p></div>
    <div class="step"><div class="ring"><svg width="44" height="40" viewBox="0 0 44 40" fill="none" stroke="#fff" stroke-width="3"><circle cx="16" cy="22" r="9" stroke-dasharray="4 3" stroke-width="6"/><circle cx="16" cy="22" r="3"/><circle cx="34" cy="9" r="6" stroke-dasharray="3 2" stroke-width="4"/></svg></div><h4>Support</h4><p>For businesses on the Ledgerly platform who manage inventory with confidence.</p></div>
    <div class="step"><div class="ring"><svg width="38" height="38" viewBox="0 0 38 38" fill="none" stroke="#fff" stroke-width="2.5"><rect x="3" y="6" width="32" height="29"/><line x1="3" y1="14" x2="35" y2="14"/><line x1="11" y1="2" x2="11" y2="9"/><line x1="27" y1="2" x2="27" y2="9"/><path d="M9 20h4M17 20h4M25 20h4M9 27h4M17 27h4M25 27h4"/></svg></div><h4>Long Term</h4><p>For businesses on the Ledgerly platform who manage inventory with confidence.</p></div>
  </div>
</section>

<section class="blog">
  <h2 class="sec-title">Latest <span>Blog</span></h2>
  <p class="sec-lead">For businesses on the Ledgerly platform who manage inventory, our Scoping Consultation is the first step to finally control your inventory with confidence.</p>
  <div class="wrap posts">
    <article class="post"><div class="thumb" role="img" aria-label="Photograph of hands working with digital charts" style="background:linear-gradient(135deg,#4d6b7d,#c9b9a3)"></div><h4>4 retail technology integrations</h4><div class="meta"><span>27 MARCH 2017</span><span>120</span><span>LIKE</span><span>SHARE</span></div><p>It was only recently that I began to appreciate the enormous potential of experiential learning. Two weeks completing complex tasks with and without adequate...</p></article>
    <article class="post"><div class="thumb" role="img" aria-label="Photograph of a blue technology network scene" style="background:linear-gradient(135deg,#2c5f9e,#a9c6e4)"></div><h4>Why remote work made</h4><div class="meta"><span>27 MARCH 2017</span><span>120</span><span>LIKE</span><span>SHARE</span></div><p>It was only recently that I began to appreciate the enormous potential of experiential learning. Two weeks completing complex tasks with and without adequate...</p></article>
    <article class="post"><div class="thumb" role="img" aria-label="Photograph of a person typing on a laptop" style="background:linear-gradient(135deg,#dcdcdc,#8a8f95)"></div><h4>Why experiential learning</h4><div class="meta"><span>27 MARCH 2017</span><span>120</span><span>LIKE</span><span>SHARE</span></div><p>It was only recently that I began to appreciate the enormous potential of experiential learning. Two weeks completing complex tasks with and without adequate...</p></article>
  </div>
</section>

<section class="clients">
  <h2 class="sec-title">Working with <span>leading lights</span></h2>
  <p class="sec-lead">For businesses on the Ledgerly platform who manage inventory, our Scoping Consultation is the first step to finally control your inventory with confidence.</p>
  <div class="wrap logos">
    <div class="logo">Brannet HR</div><div class="logo">Velmar</div><div class="logo">Corvan Build</div><div class="logo">Quiet Gate</div><div class="logo">Nexora</div>
    <div class="logo">Tally 360</div><div class="logo">Brightlo</div><div class="logo">Vinteo Co</div><div class="logo">Clearmind Labs</div><div class="logo">Strivex</div>
  </div>
</section>

<section class="testimonial">
  <div class="wrap">
    <div class="t-photo" role="img" aria-label="Portrait photograph of Lena Morrow"></div>
    <div class="t-body">
      <span class="quote q-open">&ldquo;</span>
      <blockquote>For businesses on the Ledgerly platform who manage inventory, our Scoping Consultation is the first step to finally control your inventory with confidence.For businesses on the Ledgerly platform who manage inventory, our Scoping Consultation is the first step to finally control your inventory with confidence.For businesses on the Ledgerly platform who manage inventory, our Scoping Consultation is the first step to finally control your inventory with confidence.</blockquote>
      <span class="quote q-close">&rdquo;</span>
      <p class="t-name">Name : Lena Morrow</p>
      <p class="t-role">Director, Civic Relief Partners</p>
      <div class="stars"><svg width="80" height="12" viewBox="0 0 80 12" fill="none" stroke="#fff"><circle cx="6" cy="6" r="4.5"/><circle cx="22" cy="6" r="4.5"/><circle cx="38" cy="6" r="4.5"/><circle cx="54" cy="6" r="4.5"/><circle cx="70" cy="6" r="4.5" fill="#fff"/></svg></div>
    </div>
  </div>
</section>

<section class="contact">
  <h2 class="sec-title">Contact <span>Us</span></h2>
  <p class="sec-lead">Located in multiple countries and with previous clients all over the world including Malaysia, UK, New Zealand and USA</p>
  <div class="wrap contact-grid">
    <div>
      <div class="form">
        <div class="field">Name :</div><div class="field">Email :</div>
        <div class="field">Phone :</div><div class="field">Subjects :</div>
        <div class="field msg">Message :</div>
      </div>
      <div class="submit" style="margin-top:20px">SUBMIT</div>
    </div>
    <div class="info">
      <p>Located in multiple countries and with previous clients all over the world including Malaysia, UK, New Zealand and USA. For any simple queries, or if you want to catch up you can email or call us, we're always happy to talk.</p>
      <div class="info-cols">
        <div><h5>Address</h5>12/04 Harbour Rd, Melbourne,<br>VIC, 3000</div>
        <div><h5>Email Address</h5>General : enquiries@pelrandata.example<br>Office : enquiries@pelrandata.example</div>
        <div><h5>Phone</h5>Mobile : +61 (03) 9000 0000</div>
        <div><h5>Follow Us</h5><div class="social"><i></i><i></i><i></i><i></i><i></i></div></div>
      </div>
    </div>
  </div>
</section>

<footer class="site-footer">© Copyright 2017 Pelran Data.All Rights Reserved</footer>

</body>
</html>
```